Business card for IT company

Looking for a business card for an IT company providing server, network, and application support to medium businesses. Company name is Halvern Systems. Website is www.halvernsystems.example, would like to use the green color that is on the homepage. Prefer design to be done in Illustrator. Please, only DESIGNERS apply - no PHP programmers attempting to do design. Thank you

Industry/Entity Type

Information Technology

Requirements
Must have
• Green
Should not have
• Template designs, or designs done by non-designer type people

```html
<!DOCTYPE html>
<html lang="en">
<head>
<meta charset="utf-8">
<title>Halvern Systems – Business Card</title>
<link href="https://fonts.googleapis.com/css2?family=Lato:wght@400;700;900&family=Open+Sans:wght@400;600;700&display=swap" rel="stylesheet">
<style>
  :root {
    --brand-green: #6fa535;
    --brand-green-dark: #5e9a2a;
    --brand-green-light: #7db53d;
    --card-white: #ffffff;
    --ink: #2a2a2a;
    --backdrop: #2e2e2e;
  }
  * { box-sizing: border-box; margin: 0; padding: 0; }
  html, body {
    width: 1200px; height: 997px; overflow: hidden;
    background: var(--backdrop);
  }
  .canvas {
    position: relative; width: 1200px; height: 997px;
  }
  .card {
    position: absolute;
    width: 580px; height: 332px;
    border-radius: 22px;
    left: 310px;
    overflow: hidden;
  }
  /* Front */
  .card-front {
    top: 110px;
    background: linear-gradient(135deg, var(--brand-green-light), var(--brand-green-dark));
    display: flex; flex-direction: column; align-items: center; justify-content: center;
  }
  .front-mark {
    width: 110px; height: 110px; border-radius: 50%;
    background: var(--card-white);
    margin-bottom: 18px;
  }
  .front-name {
    font-family: "Lato", sans-serif; font-weight: 400;
    font-size: 34px; letter-spacing: 2px;
    color: var(--card-white); text-transform: uppercase;
  }
  /* Back */
  .card-back {
    top: 530px;
    background: var(--card-white);
  }
  .back-brand {
    position: absolute; top: 30px; right: 34px;
    display: flex; flex-direction: column; align-items: center;
  }
  .back-mark {
    width: 62px; height: 62px; border-radius: 50%;
    background: var(--brand-green); margin-bottom: 8px;
  }
  .back-name {
    font-family: "Lato", sans-serif; font-weight: 400;
    font-size: 19px; letter-spacing: 1px;
    color: var(--brand-green); text-transform: uppercase;
  }
  .divider {
    position: absolute; top: 150px; left: 300px; right: 34px;
    height: 2px; background: var(--brand-green);
  }
  .person {
    position: absolute; left: 40px; top: 156px; right: 34px;
  }
  .person-name-row { display: flex; align-items: flex-end; }
  .person-name {
    font-family: "Lato", sans-serif; font-weight: 900;
    font-size: 20px; color: var(--brand-green); text-transform: uppercase;
  }
  .person-rule {
    flex: 1; height: 2px; background: var(--brand-green);
    margin: 0 0 6px 12px; max-width: 190px;
  }
  .person-title {
    font-family: "Lato", sans-serif; font-weight: 900;
    font-size: 13px; color: var(--ink); text-transform: uppercase;
    margin-top: 2px;
  }
  .contact-list {
    list-style: none; margin-top: 16px;
  }
  .contact-item {
    display: flex; align-items: center; gap: 12px;
    font-family: "Open Sans", sans-serif; font-size: 14px; color: var(--ink);
    margin-bottom: 6px;
  }
  .contact-icon {
    width: 18px; height: 18px; flex: none;
  }
  .website {
    position: absolute; right: 34px; bottom: 82px;
    font-family: "Open Sans", sans-serif; font-weight: 700;
    font-size: 13px; color: var(--brand-green);
  }
</style>
</head>
<body>
<main class="canvas">
  <section class="card card-front" aria-label="Card front">
    <div class="front-mark"></div>
    <p class="front-name">Halvern Systems</p>
  </section>

  <section class="card card-back" aria-label="Card back">
    <div class="back-brand">
      <div class="back-mark"></div>
      <p class="back-name">Halvern Systems</p>
    </div>
    <div class="divider"></div>

    <div class="person">
      <div class="person-name-row">
        <h1 class="person-name">Clara Whitfield</h1>
        <span class="person-rule"></span>
      </div>
      <p class="person-title">Founder &amp; CEO</p>

      <ul class="contact-list">
        <li class="contact-item">
          <svg class="contact-icon" viewBox="0 0 18 18" aria-hidden="true">
            <circle cx="9" cy="9" r="9" fill="var(--brand-green)"/>
            <path d="M5 8.5c0-1.6 1.8-2.6 4-2.6s4 1 4 2.6l-1.6.6-.6-1.4H7.2l-.6 1.4z" fill="#fff"/>
            <rect x="6.5" y="9.5" width="5" height="3" rx="1" fill="#fff"/>
          </svg>
          0400 555 218 / +61 400 555 218
        </li>
        <li class="contact-item">
          <svg class="contact-icon" viewBox="0 0 18 18" aria-hidden="true">
            <circle cx="9" cy="9" r="9" fill="var(--brand-green)"/>
            <rect x="4.5" y="6" width="9" height="6.5" rx="1" fill="#fff"/>
            <path d="M4.8 6.4 9 9.6l4.2-3.2" stroke="var(--brand-green)" stroke-width="1" fill="none"/>
          </svg>
          info@larkmeadstudio.example
        </li>
        <li class="contact-item">
          <svg class="contact-icon" viewBox="0 0 18 18" aria-hidden="true">
            <circle cx="9" cy="9" r="9" fill="var(--brand-green)"/>
            <circle cx="9" cy="9" r="3.5" fill="#fff"/>
          </svg>
          clara.larkmeadstudio
        </li>
        <li class="contact-item">
          <svg class="contact-icon" viewBox="0 0 18 18" aria-hidden="true">
            <circle cx="9" cy="9" r="9" fill="var(--brand-green)"/>
            <path d="M9 14s-3.5-3.6-3.5-6a3.5 3.5 0 0 1 7 0c0 2.4-3.5 6-3.5 6z" fill="#fff"/>
            <circle cx="9" cy="8" r="1.3" fill="var(--brand-green)"/>
          </svg>
          PO Box 2184,QLD 4012
        </li>
      </ul>
    </div>

    <p class="website">www.halvernsystems.example</p>
  </section>
</main>
</body>
</html>
```